Our company TrulaPay, an online processor of payments is seeking talented submissions for our website redesign. The winning design will be chopped up and converted into a WordPress theme to allow for easy content additions and updates.

We are looking for modern designs that rival current websites in our industry (plimo.example, zanquetto.example, holvix.example, brandle.example, quillmarkcharges.example, evensplitcharges.example, KoboRun.example).

Our company is seeking to expand our reach to software developers and engineers who are either integrating our payment platform into their offerings or are engineering a custom solution for the company they work for and are in need of a payment platform such as our own.

We currently work with hundreds of different business partners whom either resell our services or integrate our processing capabilities into their software (which they sell). We also must communicate effectively to end users, businesses, who seek us out directly for their payment processing needs.

We are open to different color schemes but would ultimately like them to be somewhat inline with our current logo (see attached). Our website needs to instill security and confidence to any current and/or potential user as we are trusted with private and sensitive information.

We are seeking submissions from qualified; individual freelancers, freelance teams, and agencies who can attack this project in its entirety. Since this project is a total redesign, we would like submissions that have the capability to design any custom graphics, icons, buttons, and illustrations in line with our industry, capabilities, offerings, and content. We are looking for someone to design our new website and would prefer a vendor who can also help us to design elements (graphics, illustrations, charts, workflows) within our website.

Designs will be converted into a wordpress theme and we would like to utilize widgets for as many areas as possible to make editing and updating easy.

We are seeking the creation of a few unique pages but many of the pages for the majority of our content will just be internal content pages which will be duplicated.

We will likely contract with the winning submission for future work.

Please see Design Reference Document for more information

Target Market(s)

Resellers
Merchant Service Providers
Software Developers
Independent Sales Organizations (ISOs)
App Builders
Mobile App Builders
Independent Software Developers
Organizational Software Developers
Businesses who need to accept payments
Governments
Municipalities
Schools
DMVs
Courts
Retailers
Medical Offices
Hosipitals
Clinics
Dr. Offices
Gyms
Churches
Non-Profits
Software Companies
Technology Companies
Startups

• Logo cannot change drastically.

```html
<!DOCTYPE html>
<html lang="en">
<head>
<meta charset="utf-8">
<title>TrulaPay API Overview</title>
<link rel="stylesheet" href="https://fonts.googleapis.com/css2?family=Arimo:wght@400;700&family=Open+Sans:wght@400;700&display=swap">
<style>
:root{
  --teal:#3790ac;
  --band-line:#d4d6d8;
  --panel:#d9d9d9;
  --subpanel:#e9e9e9;
  --white:#ffffff;
  --ink:#3f3f3f;
  --ink-dark:#1f2a2e;
  --rule:#b9b9b9;
  --footer:#323537;
  --footer-ink:#e6e6e6;
  --link:#3a9bbd;
  --muted:#8c8f91;
}
*{box-sizing:border-box;margin:0;padding:0}
html,body{width:1200px;height:847px;overflow:hidden}
body{position:relative;background:var(--white);font-family:"Arimo",Arial,sans-serif;color:var(--ink)}
.abs{position:absolute}
.header-band{left:0;top:0;width:1200px;height:265px;background:var(--teal)}
.header-line{left:0;top:265px;width:1200px;height:5px;background:var(--band-line)}
.brand{left:312px;top:18px;color:var(--white);font-size:14px;display:flex;align-items:center;gap:3px;letter-spacing:-.2px}
.brand .dot{width:4px;height:4px;border-radius:50%;background:var(--white);margin-top:6px}
.main-nav{top:22px;left:407px;display:flex;gap:11px;font-size:6.8px;color:var(--white);letter-spacing:.1px}
.main-nav span{display:flex;align-items:center;gap:3px}
.util-nav{top:24px;left:665px;display:flex;gap:6px;font-size:6.2px;color:var(--white)}
.search{left:820px;top:23px;display:flex;height:9px}
.search .field{width:42px;background:var(--white)}
.search .btn{width:25px;background:#25333a;color:var(--white);font-size:6px;text-align:center;line-height:9px}

.shell{left:312px;top:57px;width:576px;height:601px;background:var(--white);border-radius:10px}
.content{left:456px;top:57px;width:432px;height:601px;background:var(--panel);border-radius:10px}

.side-item{position:absolute;left:323px;display:flex;align-items:center;font-size:7.5px;color:#444;letter-spacing:.2px}
.side-item svg{width:12px;height:12px;margin-left:9px;margin-right:11px}
.side-item.active{top:73px;width:140px;height:24px;background:var(--panel);border-radius:12px 0 0 12px}
.tutorials{left:323px;top:103px;width:121px;height:136px;background:var(--subpanel);border-radius:12px}
.tutorials .head{position:absolute;top:5px;left:0;width:121px;display:flex;align-items:center;font-size:7.5px;letter-spacing:.2px}
.tutorials .head svg{width:12px;height:12px;margin-left:9px;margin-right:11px}
.tutorials .caret{position:absolute;right:12px;top:2px}
.tutorials ul{position:absolute;left:11px;top:24px;list-style:none;font-size:5.6px;line-height:9.6px;color:#555}

.title{left:487px;top:79px;font-size:12.5px;color:#333;font-weight:400}
.lede{left:487px;top:102px;width:208px;font-size:7px;line-height:8.4px}
.card{background:var(--white);border-radius:14px}
.card-start{left:724px;top:80px;width:134px;height:72px}
.card-start h3{position:absolute;top:10px;left:0;width:134px;text-align:center;font-size:7px;color:#222}
.card-start p{position:absolute;left:9px;top:27px;width:114px;font-size:5.8px;line-height:8.3px}
.rule{left:543px;width:255px;height:1px;background:var(--rule)}
.sec-head{left:486px;font-size:7px;color:#333}
.sec-body{left:486px;width:374px;font-size:7px;line-height:8.4px}
.feature{top:355px;width:177px;height:109px}
.feature h4{position:absolute;left:12px;top:12px;font-size:8.5px;color:var(--ink-dark)}
.feature p{position:absolute;left:12px;top:29px;width:152px;font-size:7px;line-height:8.4px}
.def-term{left:486px;font-size:6.8px;font-weight:700;color:#222}

.footer{left:0;top:699px;width:1200px;height:148px;background:var(--footer)}
.foot-brand{left:312px;top:727px;font-size:13px;color:var(--muted);display:flex;align-items:center;gap:3px}
.foot-brand .dot{width:4px;height:4px;border-radius:50%;background:var(--muted);margin-top:6px}
.foot-col{font-family:"Open Sans",Arial,sans-serif;color:var(--footer-ink);font-size:6.6px;line-height:11px}
.foot-col h5{font-size:6.6px;font-weight:700;color:var(--white);letter-spacing:.2px}
.foot-col .small{font-size:5.6px;line-height:7px}
.foot-col a{color:var(--link);text-decoration:none}
.social{left:738px;top:727px;display:flex;gap:7px}
.social span{width:13px;height:13px;background:var(--footer-ink);border-radius:2px}
</style>
</head>
<body>
<div class="abs header-band"></div>
<div class="abs header-line"></div>

<div class="abs brand">TrulaPay<span class="dot"></span></div>
<nav class="abs main-nav">
  <span>DOCUMENTATION</span>
  <span>ABOUT <svg width="5" height="4" viewBox="0 0 5 4"><path d="M.5 1 2.5 3 4.5 1" stroke="#fff" fill="none" stroke-width=".8"/></svg></span>
  <span>SUPPORT</span>
</nav>
<div class="abs util-nav"><span>CALL US ON: 555 014 2270</span><span>EMAIL US</span><span>LOGIN</span></div>
<div class="abs search"><div class="field"></div><div class="btn">search</div></div>

<div class="abs shell"></div>
<div class="abs content"></div>

<!-- Sidebar -->
<div class="side-item active">
  <svg viewBox="0 0 12 12"><path d="M1 6c2-3.5 8-3.5 10 0-2 3.5-8 3.5-10 0z" fill="#555"/><circle cx="6" cy="6" r="1.8" fill="#d9d9d9"/></svg>OVERVIEW
</div>
<div class="abs tutorials">
  <div class="head">
    <svg viewBox="0 0 12 12"><path d="M1.5 6 3 2h6l1.5 4v4h-9z" fill="none" stroke="#555" stroke-width="1.2"/><path d="M1.5 6h3l.5 1.3h2L7.5 6h3" fill="none" stroke="#555" stroke-width="1.2"/></svg>TUTORIALS
    <svg class="caret" width="9" height="6" viewBox="0 0 9 6"><path d="M1 1l3.5 3.5L8 1" stroke="#555" fill="none" stroke-width="1.2"/></svg>
  </div>
  <ul>
    <li>Making API calls</li><li>Charge a customer</li><li>Tokenization</li><li>Refund a payment</li>
    <li>Instant Payment Notifications</li><li>Subscriptions</li><li>Batch Calls</li>
    <li>Connect Web Analytics</li><li>Customization</li><li>Mobile Integration (beta)</li><li>Upgrade API Version</li>
  </ul>
</div>
<div class="side-item" style="top:252px"><svg viewBox="0 0 12 12"><circle cx="6" cy="2" r="1.2" fill="none" stroke="#444"/><path d="M6 3.2V11M3.5 5h5M1.5 7.5C2 10 4 11 6 11s4-1 4.5-3.5" fill="none" stroke="#444" stroke-width="1.1"/></svg>PLATFORM TUTORIALS</div>
<div class="side-item" style="top:281px"><svg viewBox="0 0 12 12"><path d="M2 10.5 7 5.5M7.5 1.5a2.8 2.8 0 0 0 3 3L9 6 6 3z" stroke="#444" stroke-width="1.6" fill="#444"/></svg>SDKS AND PLUGINS</div>
<div class="side-item" style="top:310px"><svg viewBox="0 0 12 12"><path d="M2 10.5l1-3 6-6 2 2-6 6z" fill="#444"/></svg>PREFERENCES</div>
<div class="side-item" style="top:339px"><svg viewBox="0 0 12 12"><circle cx="6" cy="6" r="5" fill="#444"/><circle cx="6" cy="6" r="3.5" fill="none" stroke="#777" stroke-width=".6"/></svg>API CALLS</div>
<div class="side-item" style="top:368px"><svg viewBox="0 0 12 12"><path d="M6 1v5M3.3 3a4 4 0 1 0 5.4 0" stroke="#444" stroke-width="1.3" fill="none"/></svg>BUTTONS</div>
<div class="side-item" style="top:397px"><svg viewBox="0 0 12 12"><path d="M4.5 1h3l1 4h-5zM3 6h6l1 4H2zM1 10.5h10v1H1z" fill="#444"/></svg>SUPPORT</div>
<div class="side-item" style="top:426px"><svg viewBox="0 0 12 12"><circle cx="3.5" cy="7" r="1.8" fill="none" stroke="#555"/><circle cx="8.5" cy="7" r="1.8" fill="none" stroke="#555"/><path d="M5.3 7h1.4" stroke="#555"/></svg>FAQ</div>

<!-- Content -->
<h1 class="abs title">TrulaPay API Overview</h1>
<p class="abs lede">Jujubes jelly beans pastry cake biscuit jujubes cheesecake. Chocolate bar chocolate bar topping lemon drops tootsie roll. Macaroon chocolate bar sweet tart powder tootsie roll macaroon liquorice.</p>
<div class="abs card card-start">
  <h3>Get ready to get started</h3>
  <p>Jujubes jelly beans pastry cake biscuit jujubes cheesecake. Chocolate bar chocolate bar topping lemon drops tootsie roll. Macaroon chocolate bar sweet tart</p>
</div>

<div class="abs rule" style="top:160px"></div>
<div class="abs sec-head" style="top:170px">Jujubes jelly beans pastry cake biscuit jujubes</div>
<p class="abs sec-body" style="top:190px">Jujubes jelly beans pastry cake biscuit jujubes cheesecake. Chocolate bar chocolate bar topping lemon drops tootsie roll. Macaroon chocolate bar sweet tart powder tootsie roll macaroon liquorice.<br>Bonbon carrot cake tart. Danish dessert danish croissant topping biscuit. Candy lollipop lemon drops tart muffin bear claw gummi bears softknit.example carrot cake.<br>Carrot cake carrot cake croissant tiramisu. Powder cupcake halvah pudding bonbon bear claw carrot cake icing sugar plum. Lollipop cake muffin dessert gummies biscuit oat cake jujubes.</p>

<div class="abs rule" style="top:253px"></div>
<div class="abs sec-head" style="top:264px">Jujubes jelly beans pastry cake biscuit jujubes</div>
<p class="abs sec-body" style="top:284px">Jujubes jelly beans pastry cake biscuit jujubes cheesecake. Chocolate bar chocolate bar topping lemon drops tootsie roll. Macaroon chocolate bar sweet tart powder tootsie roll macaroon liquorice.<br>Bonbon carrot cake tart. Danish dessert danish croissant topping biscuit. Candy lollipop lemon drops tart muffin bear claw gummi bears softknit.example carrot cake.<br>Carrot cake carrot cake croissant tiramisu. Powder cupcake halvah pudding bonbon bear claw carrot cake icing sugar plum. Lollipop cake muffin dessert gummies biscuit oat cake jujubes.</p>

<div class="abs rule" style="top:345px"></div>
<div class="abs card feature" style="left:483px">
  <h4>Jujubes jelly beans</h4>
  <p>Jujubes jelly beans pastry cake biscuit jujubes cheesecake. Chocolate bar chocolate bar topping lemon drops tootsie roll. Macaroon chocolate bar sweet tart powder tootsie roll macaroon liquorice.<br>Bonbon carrot cake tart. Danish dessert danish croissant topping biscuit. Candy lollipop lemon drops tart muffin bear claw gummi bears</p>
</div>
<div class="abs card feature" style="left:680px">
  <h4>Jujubes jelly beans</h4>
  <p>Jujubes jelly beans pastry cake biscuit jujubes cheesecake. Chocolate bar chocolate bar topping lemon drops tootsie roll. Macaroon chocolate bar sweet tart powder tootsie roll macaroon liquorice.<br>Bonbon carrot cake tart. Danish dessert danish croissant topping biscuit. Candy lollipop lemon drops tart muffin bear claw gummi bears</p>
</div>

<div class="abs sec-head" style="top:486px">Jujubes jelly beans pastry cake biscuit jujubes</div>
<p class="abs sec-body" style="top:506px">Jujubes jelly beans pastry cake biscuit jujubes cheesecake. Chocolate bar chocolate bar topping lemon drops tootsie roll. Macaroon chocolate bar sweet tart powder tootsie roll macaroon liquorice.<br>Bonbon carrot cake tart. Danish dessert danish croissant topping biscuit. Candy lollipop lemon drops tart muffin bear claw gummi bears softknit.example carrot cake.<br>Carrot cake carrot cake croissant tiramisu. Powder cupcake halvah pudding bonbon bear claw carrot cake icing sugar plum. Lollipop cake muffin dessert gummies biscuit oat cake jujubes.</p>

<div class="abs rule" style="top:567px"></div>
<div class="abs sec-head" style="top:578px">Jujubes jelly beans pastry cake biscuit jujubes</div>
<div class="abs def-term" style="top:593px">Jujubes jelly</div>
<p class="abs sec-body" style="top:601px">beans pastry cake biscuit jujubes cheesecake.</p>
<div class="abs def-term" style="top:618px">Chocolate bar</div>
<p class="abs sec-body" style="top:626px">chocolate bar topping lemon drops tootsie roll. Macaroon chocolate bar sweet tart powder tootsie roll macaroon s tke</p>

<!-- Footer -->
<footer class="abs footer"></footer>
<div class="abs foot-brand">TrulaPay<span class="dot"></span></div>
<div class="abs foot-col" style="left:511px;top:724px;width:140px">
  <h5>CONTACT</h5>
  <div>TrulaPay</div>
  <div>Address: Lumen Way 13, 9000</div>
  <div>Tel.: 5550 14 227</div>
</div>
<div class="abs foot-col" style="left:511px;top:780px;width:140px">
  <h5>UPDATES</h5>
  <p class="small">Jujubes jelly beans pastry cake biscuit jujubes cheesecake</p>
  <p class="small" style="margin-top:6px">Jujubes jelly beans pastry cake biscuit jujubes cheesecake</p>
</div>
<div class="abs social" aria-label="Social links"><span></span><span></span><span></span><span></span><span></span></div>
<div class="abs foot-col" style="left:738px;top:761px;width:160px">
  <h5>PRESS</h5>
  <div>Press and media inquiries? Please contact us</div>
  <div>or <a href="#">download</a> a high resolution logo.</div>
</div>
<div class="abs foot-col" style="left:738px;top:813px;width:160px">
  <h5>LEGAL</h5>
  <div>Copyright © 2014 TrulaPay, All rights reserved.</div>
</div>
</body>
</html>
```